Bramble Sweet Box Box - Shopify Website Design

A monthly subscription company. Need a Shopify Website Design and uploaded to fully work with Kettle Renewals.

Please look at these sites for examples as well as the images I enclosed.

http://bramblesweetbox.example
https://www.lumora-oils.example/
https://www.plateworks.example/
https://www.globesnackery.example/
https://www.cuppaloop.example/
https://roastcrate.example/

```html
<!DOCTYPE html>
<html lang="en">
<head>
<meta charset="utf-8">
<title>Bramble Sweet Box</title>
<link rel="stylesheet" href="https://fonts.googleapis.com/css2?family=Montserrat:wght@400;500;600;700&family=Lora:wght@600;700&display=swap">
<style>
  :root {
    --blue: #1b7db3;
    --pink: #e6296f;
    --ink: #1d1d1d;
    --body: #3a3a3a;
    --line: #e3e3e3;
    --card: #f8f6f6;
    --card-line: #e4e1e1;
    --white: #ffffff;
  }
  * { box-sizing: border-box; margin: 0; padding: 0; }
  html, body { width: 1200px; height: 3065px; overflow: hidden; background: var(--white); }
  body { position: relative; font-family: "Montserrat", sans-serif; color: var(--body); }
  .abs { position: absolute; }
  .divider { position: absolute; left: 144px; width: 912px; height: 1px; background: var(--line); }

  .promo-bar { top: 0; left: 0; width: 1200px; height: 38px; background: var(--blue); color: var(--white);
    font-size: 12px; text-align: center; line-height: 38px; }

  .search { top: 66px; left: 144px; width: 166px; height: 31px; border-bottom: 1px solid #cfcfcf;
    font-size: 12px; color: #555; display: flex; align-items: center; gap: 6px; padding-bottom: 6px; }
  .brand { top: 58px; left: 0; width: 1200px; display: flex; justify-content: center; align-items: center; gap: 12px; }
  .brand-dot { width: 40px; height: 40px; border-radius: 50%; background: var(--pink); }
  .brand-name { font-weight: 700; font-size: 30px; letter-spacing: 2px; color: var(--ink); }
  .header-icons { top: 73px; left: 1005px; display: flex; gap: 14px; }

  .main-nav { top: 155px; left: 0; width: 1200px; display: flex; justify-content: center; gap: 0; font-size: 13px; color: var(--ink); }
  .main-nav a { color: inherit; text-decoration: none; position: relative; padding-bottom: 28px; }
  .main-nav a.active::after { content: ""; position: absolute; left: 0; right: 0; bottom: 0; height: 3px; background: var(--pink); }

  .hero { top: 238px; left: 144px; width: 912px; height: 462px;
    background: linear-gradient(110deg, #b54f87 0%, #9a7390 30%, #8b7a82 50%, #857d8c 70%, #6c77a6 100%); }
  .hero-text { top: 368px; left: 144px; width: 912px; text-align: center; color: var(--white); }
  .hero-title { font-family: "Lora", serif; font-weight: 700; font-size: 60px; letter-spacing: 1px; text-shadow: 0 2px 6px rgba(0,0,0,.35); }
  .hero-sub { margin-top: 26px; font-weight: 600; font-size: 16px; text-shadow: 0 1px 4px rgba(0,0,0,.4); }
  .play { top: 510px; left: 577px; width: 46px; height: 46px; border-radius: 50%; background: var(--blue); }

  .section-title { font-family: "Lora", serif; font-weight: 700; font-size: 25px; color: var(--ink); text-align: center; letter-spacing: .5px; }
  .section-title .blue { color: var(--blue); }
  .section-title .pink { color: var(--pink); }

  .welcome { top: 774px; left: 144px; width: 912px; text-align: center; }
  .welcome p { margin: 24px auto 0; width: 800px; font-size: 13px; line-height: 28px; color: var(--body); }
  .welcome .cta { display: inline-block; margin-top: 24px; font-size: 13px; font-weight: 600; color: var(--pink); text-decoration: underline; }

  .product { position: absolute; width: 295px; text-align: center; }
  .product-media { position: relative; height: 310px; background: var(--card); border: 1px solid var(--card-line); }
  .product-shot { position: absolute; left: 40px; right: 40px; top: 55px; bottom: 60px; border-radius: 4px; }
  .shot-white { background: linear-gradient(160deg, #f0f0f0, #bdbdbd 60%, #6b4a30); }
  .shot-choc { background: linear-gradient(160deg, #c8364d, #6b3f2a 40%, #3a241a); }
  .shot-kraft { background: linear-gradient(180deg, #c49a6c 0%, #c49a6c 45%, #e14b3c 60%, #8bc34a 80%, #c49a6c 100%); }
  .shot-mix { background: linear-gradient(135deg, #e0483f, #4aa3d8 45%, #f2f2f2 60%, #7ac143); }
  .badge { position: absolute; top: 16px; left: 16px; background: var(--blue); color: var(--white); font-size: 10px; font-weight: 700; padding: 6px 8px; }
  .quick-view { position: absolute; left: 30px; right: 30px; bottom: 30px; height: 40px; background: var(--white); border: 1px solid #cfcfcf;
    font-size: 11px; font-weight: 700; color: var(--ink); line-height: 38px; }
  .product-name { margin-top: 26px; font-size: 16px; font-weight: 700; color: var(--ink); letter-spacing: .3px; }
  .product-price { margin-top: 12px; font-size: 15px; color: var(--pink); }

  .promo-tile { position: absolute; top: 1984px; width: 445px; height: 545px; color: var(--white); text-align: center; }
  .tile-marsh { left: 144px; background: linear-gradient(160deg, #4a3a3e, #3a2c2a 50%, #2d2320); }
  .tile-corn { left: 612px; background: linear-gradient(160deg, #3b2b22, #4a3022 50%, #2a1d16); }
  .tile-copy { position: absolute; top: 283px; left: 0; right: 0; }
  .tile-title { font-size: 16px; font-weight: 700; letter-spacing: .4px; }
  .tile-link { display: inline-block; margin-top: 14px; font-size: 11px; color: var(--pink); text-decoration: underline; }

  .newsletter { top: 2645px; left: 144px; width: 912px; text-align: center; }
  .newsletter p { margin-top: 22px; font-size: 15px; color: var(--body); }
  .signup { top: 2773px; left: 359px; width: 481px; height: 48px; border: 1px solid #d0d0d0; display: flex; }
  .signup-input { flex: 1; font-size: 14px; color: #555; padding-left: 22px; line-height: 46px; }
  .signup-button { width: 106px; margin: 1px; background: var(--pink); color: var(--white); font-size: 14px; font-weight: 700; text-align: center; line-height: 44px; }

  .footer-nav { top: 2952px; left: 144px; display: flex; font-size: 16px; color: var(--ink); }
  .footer-nav span.sep { margin: 0 22px; color: #777; }
  .legal { top: 2996px; left: 144px; font-size: 11px; color: var(--ink); }
  .legal .sep { margin: 0 6px; }
  .social { top: 2970px; left: 920px; display: flex; gap: 20px; }
  .social span { width: 22px; height: 22px; border-radius: 50%; background: var(--ink); display: block; }
</style>
</head>
<body>
  <div class="abs promo-bar">We are offering complimentary shipping on orders over $50! Click to read our full COVID statement.</div>

  <div class="abs search">
    <svg width="11" height="11" viewBox="0 0 12 12"><circle cx="5" cy="5" r="3.8" fill="none" stroke="#333" stroke-width="1.6"/><line x1="8" y1="8" x2="11" y2="11" stroke="#333" stroke-width="1.8"/></svg>
    Search
  </div>

  <div class="abs brand">
    <span class="brand-dot"></span>
    <span class="brand-name">BRAMBLE SWEET BOX</span>
  </div>

  <div class="abs header-icons">
    <svg width="20" height="20" viewBox="0 0 20 20"><circle cx="10" cy="10" r="9" fill="none" stroke="#333" stroke-width="1.4"/><circle cx="10" cy="8" r="3.2" fill="none" stroke="#333" stroke-width="1.4"/><path d="M4.5 16c1.5-2.6 3.4-3.6 5.5-3.6s4 1 5.5 3.6" fill="none" stroke="#333" stroke-width="1.4"/></svg>
    <svg width="18" height="20" viewBox="0 0 18 20"><path d="M2 6h14l-1 13H3z" fill="none" stroke="#333" stroke-width="1.4"/><path d="M6 8V4a3 3 0 0 1 6 0v4" fill="none" stroke="#333" stroke-width="1.4"/></svg>
  </div>

  <nav class="abs main-nav">
    <a class="active" href="#" style="margin-right:42px">HOME</a>
    <a href="#" style="margin-right:35px">SHOP <svg width="9" height="6" viewBox="0 0 9 6"><path d="M0 0h9L4.5 6z" fill="#1d1d1d"/></svg></a>
    <a href="#" style="margin-right:39px">SUBSCRIPTION</a>
    <a href="#" style="margin-right:42px">ABOUT US</a>
    <a href="#">CONTACT</a>
  </nav>
  <div class="divider" style="top:202px"></div>

  <div class="abs hero" role="img" aria-label="Box of assorted chocolate truffles on pink, grey and blue paper"></div>
  <div class="abs hero-text">
    <div class="hero-title">BRAMBLE SWEET BOX</div>
    <div class="hero-sub">Lorem ipsum dolor sit amet consectetur adipiscing elit</div>
  </div>
  <svg class="abs play" viewBox="0 0 46 46"><path d="M18 13l15 10-15 10z" fill="#fff"/></svg>

  <div class="divider" style="top:739px"></div>

  <section class="abs welcome">
    <h2 class="section-title">WELCOME TO <span class="blue">BRAMBLE SWEET</span> <span class="pink">BOX</span></h2>
    <p>Lorem ipsum dolor sit amet, consectetur adipiscing elit, sed do eiusmod tempor incididunt ut labore et dolore magna aliquis ipsum suspendisse ultriceus commodo viverra maecenas accumsan lacus vel facilisisorem ipsum dolor sit ametnsectetur adipisced do eiusmod tempor incididunt ut labore et dolore magna aliquis ipsum suspendisse ultriceu</p>
    <a class="cta" href="#">SCHEDULE YOUR CONSULTION TODAY</a>
  </section>

  <div class="divider" style="top:1002px"></div>

  <article class="product" style="top:1061px;left:144px">
    <div class="product-media"><div class="product-shot shot-white" role="img" aria-label="Open white gift box of chocolates"></div></div>
    <div class="product-name">PRODUCT NAME</div><div class="product-price">$56.87</div>
  </article>
  <article class="product" style="top:1061px;left:453px">
    <div class="product-media"><div class="product-shot shot-choc" role="img" aria-label="Red box of assorted chocolates" style="bottom:105px"></div><div class="quick-view">QUICK VIEW</div></div>
    <div class="product-name">PRODUCT NAME</div><div class="product-price">$56.87</div>
  </article>
  <article class="product" style="top:1061px;left:761px">
    <div class="product-media"><span class="badge">SAVE $56</span><div class="product-shot shot-kraft" role="img" aria-label="Kraft box filled with fruit candies"></div></div>
    <div class="product-name">PRODUCT NAME</div><div class="product-price">$56.87</div>
  </article>

  <article class="product" style="top:1477px;left:144px">
    <div class="product-media"><div class="product-shot shot-kraft" role="img" aria-label="Open kraft box of colourful candies"></div></div>
    <div class="product-name">PRODUCT NAME</div><div class="product-price">$56.87</div>
  </article>
  <article class="product" style="top:1477px;left:453px">
    <div class="product-media"><div class="product-shot shot-mix" role="img" aria-label="Divided tray of assorted sweets" style="left:12px;right:12px"></div></div>
    <div class="product-name">PRODUCT NAME</div><div class="product-price">$56.87</div>
  </article>
  <article class="product" style="top:1477px;left:761px">
    <div class="product-media"><div class="product-shot shot-kraft" role="img" aria-label="Kraft box of gummy candies"></div></div>
    <div class="product-name">PRODUCT NAME</div><div class="product-price">$56.87</div>
  </article>

  <div class="divider" style="top:1931px"></div>

  <div class="promo-tile tile-marsh" role="img" aria-label="Wooden tray of marshmallows and jelly beans">
    <div class="tile-copy"><div class="tile-title">SED UT PERSPICIATIS UNDEOM</div><a class="tile-link" href="#">SHOP NOW</a></div>
  </div>
  <div class="promo-tile tile-corn" role="img" aria-label="Wooden crate of candy corn and sprinkles">
    <div class="tile-copy"><div class="tile-title">SED UT PERSPICIATIS UNDEOM</div><a class="tile-link" href="#">SHOP NOW</a></div>
  </div>

  <div class="divider" style="top:2578px"></div>

  <section class="abs newsletter">
    <h2 class="section-title">SUBSCRIBE TO <span class="blue">OUR</span> <span class="pink">NEWSLETTER</span></h2>
    <p>Sign up to our newsletter to receive updates about our future roasts!</p>
  </section>
  <div class="abs signup">
    <div class="signup-input">Enter Email</div>
    <div class="signup-button">SUBSCRIBE</div>
  </div>

  <div class="divider" style="top:2889px"></div>

  <footer>
    <div class="abs footer-nav">
      <span>HOME</span><span class="sep">|</span><span>SHOP</span><span class="sep">|</span><span>SUBSCRIPTION</span><span class="sep">|</span><span>ABOUT US</span><span class="sep">|</span><span>CONTACT</span>
    </div>
    <div class="abs legal">© 2020 Bramble Sweet Box.All Rights Reserved<span class="sep">|</span>Privacy Policy<span class="sep">|</span>Terms and Use</div>
    <div class="abs social" aria-label="Social links">
      <span></span><span></span><span></span><span></span>
    </div>
  </footer>
</body>
</html>
```